Training program workbook Cover & Insert

We need a cover for a training manual for a Management and leadership program & the first topic title page.

We are an executive consultation business that develops training programs and provides in-house strategic support for businesses across different sectors. We see this will be an ongoing design project as we will be creating a cover for the folder (to be inserted into the A4 binder) and then as we develop the sections a series of title pages for each topic.
We are currently looking for designs for the Main cover and first topic ( 2 x A4 pages / like a double sided flyer really). The designs should reflect
- sophistication
- growth
- drive
- fun
- agility
With a theme that can be replicated across a series of topics e.g. communication, time effectiveness, conflict resolution etc etc

The Program is called "PIVOT".
The tagline for the binder cover is
"Creating Leadership Agility in a Changing World"

The first topic is "TIME"
Tagline
Living & Working in "REAL" Time

We are open to any colour other than orange.

Target Market(s)

Training Program participants

Industry/Entity Type

Training

Font styles to use
Serif

Colors

Designer to choose colors to be used in the design.

Requirements
Must have
• A design framework that can be expanded for various topic cover pages within the manual.
• Eye Catching graphics that excite the viewer and entice them to continue reading
Nice to have
• Copyright (symbol) Marlowe Group in small font at the bottom of the page
Should not have
• Typical daggy old school training images

```html
<!DOCTYPE html>
<html lang="en">
<head>
<meta charset="utf-8">
<title>Marlowe Group – Management and Leadership Training Program</title>
<link rel="stylesheet" href="https://fonts.googleapis.com/css2?family=Sorts+Mill+Goudy&display=swap">
<style>
  :root {
    --paper: #ffffff;
    --ink: #1c1c1c;
    --brand-ink: #2b2b2b;
    --box-top: #857050;
    --box-side: #63533a;
    --box-face: #dedede;
    --box-edge: #a88a5e;
    --word-gold: #c9a97c;
    --band: #d2b086;
    --band-rule: #ffffff;
  }
  * { margin: 0; padding: 0; box-sizing: border-box; }
  html, body { width: 848px; height: 1200px; overflow: hidden; background: var(--paper); }
  .cover {
    position: relative;
    width: 848px;
    height: 1200px;
    background: var(--paper);
    font-family: "Sorts Mill Goudy", Georgia, serif;
    color: var(--ink);
  }
  .brand {
    position: absolute;
    left: 51px;
    top: 58px;
    display: flex;
    align-items: center;
    gap: 10px;
    font-size: 26px;
    color: var(--brand-ink);
  }
  .brand-mark {
    width: 16px;
    height: 16px;
    background: var(--word-gold);
  }
  .program-title {
    position: absolute;
    left: 0;
    top: 142px;
    width: 100%;
    text-align: center;
    font-size: 55px;
    font-weight: 400;
    line-height: 68px;
    letter-spacing: 0.5px;
  }
  .program-box {
    position: absolute;
    left: 0;
    top: 0;
  }
  .program-name {
    position: absolute;
    left: 238px;
    top: 580px;
    width: 440px;
    text-align: center;
    font-size: 112px;
    line-height: 1;
    color: var(--word-gold);
    text-shadow: 4px 6px 6px rgba(40, 30, 15, 0.75);
  }
  .tagline-band {
    position: absolute;
    left: 0;
    top: 956px;
    width: 848px;
    height: 124px;
    background: var(--band);
    box-shadow: 0 0 8px 3px rgba(210, 176, 134, 0.8);
  }
  .tagline {
    position: absolute;
    left: 51px;
    top: 14px;
    width: 747px;
    height: 98px;
    border: 1px solid var(--band-rule);
    display: flex;
    align-items: center;
    justify-content: center;
    text-align: center;
    font-size: 35px;
    line-height: 50px;
    color: var(--ink);
  }
  .copyright {
    position: absolute;
    left: 51px;
    top: 1148px;
    font-size: 21px;
    letter-spacing: 0.5px;
  }
</style>
</head>
<body>
<main class="cover">
  <div class="brand"><span>Marlowe Group</span><span class="brand-mark"></span></div>

  <h1 class="program-title">Management and Leadership<br>Training Program</h1>

  <svg class="program-box" width="848" height="1200" viewBox="0 0 848 1200" aria-hidden="true">
    <polygon points="146,396 586,334 678,384 238,448" fill="var(--box-top)"/>
    <polygon points="146,396 238,448 238,902 145,852" fill="var(--box-side)"/>
    <polygon points="238,448 678,386 678,840 238,902" fill="var(--box-face)" stroke="var(--box-edge)" stroke-width="2.5"/>
  </svg>
  <div class="program-name">Pivot</div>

  <section class="tagline-band">
    <p class="tagline">“Creating Leadership Agility in<br>a Changing World”</p>
  </section>

  <p class="copyright">© Marlowe Group 2017</p>
</main>
</body>
</html>
```